依頼詳細
記載項目の内容を含んだ、 85.6mm × 54.0mmのICカード(一般的なカードと同じサイズ)に印刷可能なデザインをお願い致します。
カードは横向きなので、縦向きのデザインは不可と致します。

(1)弊社のロゴ(※添付ファイル)に合うもの
(2)「ハイテクさ(技術力)」「クリーンさ(清潔感)」
が感じられるデザインを求めております。

※ロゴの配色は、添付ファイルのもの(グラデーション)からデザインに合わせて変更し単色等にして頂いても問題ありません

・トンボ(トリムマーク)をつけて下さい。
・フチなしのデザインなどは必ず仕上がり線より外側に3mm程度の塗り足しを入れて下さい。
・顔写真または半身写真など:仮として、グレーに塗りつぶした人物のシルエットでデザインに入れ込んでください。
記載項目
●表面内容
①名前欄
②社員番号欄
③発行日欄
④顔写真欄
⑤会社名:KVT株式会社
⑥本社住所
〒241-0815
神奈川県相模原市南区北見坂3丁目8番21号
TEL 042-618-3940(代表) FAX 042-619-2856
⑦「上記のものは当社の従業員であることを証明する」の一文

●裏面内容
・弊社の経営理念
「時代と共に進化を続け、最適な快適環境を提供する」

・注意事項
本証は当社社員であることを証明するものである
このカードを他人に貸与又は譲渡しないこと
本証は常時携帯すること
本証を紛失、破損した場合は直ちに届け出ること
退職時は直ちに返納すること
本証を取得された方は当社にご連絡ください
希望イメージ
シンプル 複雑
単色 カラフル
暗い 明るい
日常 高級
遊び心 厳粛
未来的 伝統的
女性的 男性的
希望する色
青系、緑系、グレー系
納品ファイル
• 高解像度JPG (.jpg)
• イラストレーター形式 (.ai)
• フォトショップ形式 (.psd)
• PNG形式 (.png)
補足説明
他社の知的財産権・商標を侵すようなデザイン等の提案は決してしないようにお願い致します。
著作権の盗用や侵害するデザイン案は厳禁になります。
素材テンプレートの流用やアレンジも不可です。
皆様からのご提案、誠にありがとうございます。
よりイメージの付きやすいデザインが可能となるよう、希望内容を追記させていただく事となりました。
ご一読の程、よろしくお願い致します。

●追加希望内容
カラーはグラデーション等の効果よりも、シンプルなものがベストです
依頼内容を明確にするため、さらに追加したい点がございましたので、期間延長の上追記させて頂きます。ご確認の程よろしくお願い致します。

●写真のサイズは免許証と同じ程度の大きさでお願い致します
●写真素材を使用したものよりも、デザインのみのシンプルなものがベストです

表面・裏面共にシンプルかつスマートなデザインで、弊社内でも最も多数から好評でありましたので当選とさせて頂きました。

今回のコンペにご参加頂きました皆様、素晴らしいデザイン案を多数頂きまして誠にありがとうございます。

次回募集を行う事がございましたら、改めましてご参加頂ければ幸いです。

```html
<!DOCTYPE html>
<html lang="ja">
<head>
<meta charset="utf-8">
<title>KVT ID Card</title>
<link rel="stylesheet" href="https://fonts.googleapis.com/css2?family=Noto+Sans+JP:wght@400;500;700&family=Noto+Serif+JP:wght@500;700&display=swap">
<style>
:root{
  --bg:#d9dadc;
  --card:#ffffff;
  --blue:#1f6fc4;
  --blue-dark:#0f4f9c;
  --blue-light:#5aa7e6;
  --ink:#333;
  --grey:#8a8d92;
  --photo:#bfc2c6;
  --rule:#c9ccd0;
}
*{margin:0;padding:0;box-sizing:border-box}
html,body{width:897px;height:1200px;overflow:hidden}
body{background:var(--bg);font-family:"Noto Sans JP",sans-serif;color:var(--ink);position:relative}
.card{position:absolute;left:105px;width:687px;height:418px;background:var(--card);border-radius:18px;overflow:hidden}
.card--front{top:105px}
.card--back{top:643px}
.wave{position:absolute;left:0;bottom:0;width:100%;height:110px}

/* front */
.brand{position:absolute;left:28px;top:26px;display:flex;align-items:center;gap:10px}
.brand__dot{width:30px;height:30px;border-radius:50%;background:var(--blue)}
.brand__name{font-size:32px;font-weight:700;color:var(--blue-dark);letter-spacing:.5px}
.brand__tag{position:absolute;left:275px;top:32px;background:var(--blue);color:#fff;font-size:15px;font-weight:500;padding:4px 14px;letter-spacing:1px}
.header-rule{position:absolute;left:0;top:82px;width:380px;height:2px;background:var(--blue)}
.photo{position:absolute;left:420px;top:30px;width:240px;height:230px;background:linear-gradient(#cfd2d5,var(--photo))}
.name{position:absolute;left:30px;top:140px;font-family:"Noto Serif JP",serif;font-size:30px;font-weight:500;letter-spacing:4px}
.name-rule{position:absolute;left:30px;top:190px;width:360px;height:1px;background:var(--rule)}
.name-roman{position:absolute;left:30px;top:198px;font-family:"Noto Serif JP",serif;font-size:17px;color:#555}
.fields{position:absolute;left:330px;top:262px;font-size:11px;line-height:18px;color:#444}
.fields div{display:flex;gap:14px;border-bottom:1px solid var(--rule);width:180px}
.fields span:first-child{width:46px;color:var(--grey)}
.company{position:absolute;left:30px;top:308px;font-family:"Noto Serif JP",serif;font-size:15px;font-weight:500}
.address{position:absolute;left:200px;top:306px;font-size:10.5px;line-height:16px;color:#333}

/* back */
.motto-head{position:absolute;left:0;top:22px;width:100%;height:34px;background:linear-gradient(90deg,var(--blue),var(--blue-light) 60%,#fff);}
.motto-head span{position:absolute;left:30px;top:5px;color:#fff;font-size:17px;letter-spacing:4px;font-weight:500}
.motto{position:absolute;left:60px;top:80px;width:420px;text-align:center;font-family:"Noto Serif JP",serif;font-weight:700;color:var(--blue-dark);font-size:29px;line-height:46px;letter-spacing:1px}
.motif{position:absolute;left:505px;top:70px;width:120px;height:120px;border-radius:50%;background:#e3eef9}
.notes{position:absolute;left:30px;top:200px;width:440px;border:1px solid var(--rule);padding:8px 12px 10px}
.notes__title{display:inline-block;background:var(--blue);color:#fff;font-size:11px;padding:1px 8px;margin-bottom:5px}
.notes li{list-style:none;font-size:10.5px;line-height:17px;color:#555}
.notes li::before{content:"・"}
.back-note{position:absolute;right:30px;bottom:18px;color:#fff;font-size:11.5px}
</style>
</head>
<body>

<section class="card card--front">
  <div class="brand"><span class="brand__dot"></span><span class="brand__name">KVT Inc.</span></div>
  <div class="brand__tag">ID CARD</div>
  <div class="header-rule"></div>
  <div class="photo" role="img" aria-label="顔写真欄(グレーの人物シルエット)"></div>
  <div class="name">佐藤 健太</div>
  <div class="name-rule"></div>
  <div class="name-roman">Kenta Sato</div>
  <div class="fields">
    <div><span>社員番号</span><span>00000000</span></div>
    <div><span>発行日</span><span>2019年0月0日</span></div>
  </div>
  <div class="company">KVT株式会社</div>
  <div class="address">
    〒241-0815 神奈川県相模原市南区北見坂3丁目8番21号<br>
    TEL 042-618-3940(代表) / FAX 042-619-2856<br>
    上記のものは当社の従業員であることを証明する
  </div>
  <svg class="wave" viewBox="0 0 687 110" preserveAspectRatio="none">
    <path d="M0 70 C200 40 420 95 687 55 L687 110 L0 110 Z" fill="#5aa7e6" opacity=".5"/>
    <path d="M0 82 C220 60 440 100 687 72 L687 110 L0 110 Z" fill="#1f6fc4"/>
  </svg>
</section>

<section class="card card--back">
  <div class="motto-head"><span>経営理念</span></div>
  <div class="motto">時代と共に進化を続け、<br>最適な快適環境を提供する</div>
  <div class="motif"></div>
  <div class="notes">
    <span class="notes__title">注意事項</span>
    <ul>
      <li>本証は当社社員であることを証明するものである</li>
      <li>このカードを他人に貸与又は譲渡しないこと</li>
      <li>本証は常時携帯すること</li>
      <li>本証を紛失、破損した場合は直ちに届け出ること</li>
      <li>退職時は直ちに返納すること</li>
    </ul>
  </div>
  <svg class="wave" viewBox="0 0 687 110" preserveAspectRatio="none">
    <path d="M0 60 C200 30 420 90 687 45 L687 110 L0 110 Z" fill="#5aa7e6" opacity=".5"/>
    <path d="M0 72 C220 50 440 95 687 62 L687 110 L0 110 Z" fill="#1f6fc4"/>
  </svg>
  <div class="back-note">本証を取得された方は当社にご連絡ください</div>
</section>

</body>
</html>
```